Marlowe Tindra Pale Ale Beer Label/Badge

We need a Beer Label designed for our first official beer to be launched under The marlowe Brand!!
It will be a Pale Ale Called "Tindra Pale Ale"!

The Marlowe has the largest Craft Beer & Cider selection in the Geelong & Surf Coast region. With a funky location and a relaxed vibe, Marlowe prides itself on serving delicious, unique seasonal food paired with Australia's best Craft Beer. The marlowe is the perfect setting for a relaxed afternoon or evening with friends and can package an experience for larger groups or corporate bookings.

The Marlowe Tavern brand has been growing for over a year and a half and the first label needs to integrate The marlowe Logo but at the same time bring a fresh, new and eye catching feel to it along with embracing the "Odysseus" story in which we will be naming future beers.

The story of Tindra is found via the following link
http://en.lorevault.example/wiki/Tindra_(legend)

We expect designers to research The marlowe Tavern brand along with the all important Craft Beer Market and demographics. This will, potentially, be the start of many more labels to come for the winning designer!!

Requirements
Must have
• The original "O" needs to be integrated into the new logo and as much as the Greek mythology is being used it needs to be certain that this is an original Australian Craft Beer in the modern age!!
strong, modern & unique!!
Nice to have
• Logo could have a depiction of Tindra
Should not have
• tackiness or cheap!!

```html
<!DOCTYPE html>
<html lang="en">
<head>
<meta charset="utf-8">
<title>Marlowe Tindra Pale Ale – Label Colourways</title>
<link rel="stylesheet" href="https://fonts.googleapis.com/css2?family=Cinzel:wght@600;700&family=Cormorant+Garamond:wght@600&display=swap">
<style>
  :root {
    --ink: #4a5662;
    --cream: #fdf9e2;
    --ribbon: #4b5863;
    --seal: #9a3a32;
  }
  html, body {
    margin: 0;
    padding: 0;
    width: 1200px;
    height: 1055px;
    overflow: hidden;
    background: #ffffff;
  }
  .canvas {
    position: relative;
    width: 1200px;
    height: 1055px;
  }
  .label {
    position: absolute;
    width: 520px;
    height: 460px;
    overflow: visible;
  }
  .label--brick { left: 77px;  top: 50px;  --accent: #a9594b; --accent-dark: #94493d; }
  .label--sage  { left: 590px; top: 50px;  --accent: #56a57a; --accent-dark: #46925f; }
  .label--slate { left: 77px;  top: 519px; --accent: #58797a; --accent-dark: #4a6869; }
  .label--amber { left: 590px; top: 519px; --accent: #eba432; --accent-dark: #e39a22; }

  .frame-outline  { fill: none; stroke: var(--accent); stroke-width: 4; }
  .frame-body     { fill: var(--cream); stroke: var(--ink); stroke-width: 2.5; }
  .frame-inner    { fill: none; stroke: var(--accent); stroke-width: 1.2; opacity: .45; }
  .medallion-rim  { fill: var(--accent-dark); }
  .medallion      { fill: var(--accent); }
  .medallion-glow { fill: url(#medallionGlow); }
  .ribbon         { fill: var(--ribbon); }
  .portrait-area  { fill: var(--cream); opacity: .92; }
  .wheat-area     { fill: var(--cream); opacity: .4; }
  .seal           { fill: var(--seal); }

  .arc-title {
    font-family: "Cinzel", serif;
    font-weight: 700;
    font-size: 27px;
    letter-spacing: 1px;
    fill: var(--ink);
  }
  .arc-place {
    font-family: "Cinzel", serif;
    font-weight: 700;
    font-size: 19px;
    letter-spacing: .5px;
    fill: var(--ink);
  }
  .beer-name {
    font-family: "Cinzel", serif;
    font-weight: 600;
    font-size: 28px;
    fill: var(--cream);
  }
  .ribbon-text {
    font-family: "Cormorant Garamond", serif;
    font-weight: 600;
    font-size: 15px;
    fill: var(--cream);
  }
  .brand-name {
    font-family: "Cinzel", serif;
    font-weight: 700;
    font-size: 13px;
    letter-spacing: 1px;
    fill: var(--cream);
  }
</style>
</head>
<body>
<main class="canvas">

  <svg width="0" height="0" style="position:absolute" aria-hidden="true">
    <defs>
      <radialGradient id="medallionGlow" cx="0.4" cy="0.3" r="0.75">
        <stop offset="0" stop-color="#ffffff" stop-opacity=".38"/>
        <stop offset=".55" stop-color="#ffffff" stop-opacity=".08"/>
        <stop offset="1" stop-color="#000000" stop-opacity=".06"/>
      </radialGradient>
      <path id="titleArc" d="M 95 235 A 165 187 0 0 1 425 235"/>
      <path id="placeArc" d="M 80 235 A 180 208 0 0 0 440 235"/>
      <path id="beerArc"  d="M 150 270 A 110 95 0 0 0 370 270"/>

      <symbol id="beerLabel" viewBox="0 0 520 460" overflow="visible">
        <ellipse class="frame-outline" cx="255" cy="238" rx="195" ry="220"/>
        <ellipse class="frame-body" cx="260" cy="235" rx="190" ry="221"/>
        <ellipse class="frame-inner" cx="260" cy="235" rx="183" ry="214"/>

        <text class="arc-title"><textPath href="#titleArc" startOffset="50%" text-anchor="middle">Marlowe Tavern &amp; Brewery</textPath></text>
        <text class="arc-place"><textPath href="#placeArc" startOffset="50%" text-anchor="middle">Mount Carrow, Victoria, Australia</textPath></text>

        <g class="ribbon-left" transform="translate(20 200) rotate(38)">
          <polygon class="ribbon" points="-12,-15 14,-15 14,15 -12,15 0,0"/>
          <rect class="ribbon" x="10" y="-15" width="165" height="30"/>
          <text class="ribbon-text" x="75" y="5" text-anchor="middle">Handcrafted Beer</text>
        </g>
        <g class="ribbon-right" transform="translate(500 200) rotate(-38)">
          <polygon class="ribbon" points="12,-15 -14,-15 -14,15 12,15 0,0"/>
          <rect class="ribbon" x="-175" y="-15" width="165" height="30"/>
          <text class="ribbon-text" x="-75" y="5" text-anchor="middle">ABV 5%</text>
        </g>

        <ellipse class="medallion-rim" cx="260" cy="233" rx="120" ry="156"/>
        <ellipse class="medallion" cx="260" cy="233" rx="108" ry="144"/>
        <ellipse class="medallion-glow" cx="260" cy="233" rx="108" ry="144"/>

        <path class="wheat-area" role="img" aria-label="Wheat sprigs framing the portrait"
              d="M 172 205 Q 180 120 232 98 Q 200 135 194 215 Z M 348 205 Q 340 120 288 98 Q 320 135 326 215 Z"/>
        <ellipse class="portrait-area" role="img" aria-label="Silhouette portrait of Tindra with a spiral of hair"
                 cx="262" cy="218" rx="60" ry="70"/>

        <circle class="seal" cx="260" cy="96" r="17"/>
        <text class="brand-name" x="260" y="134" text-anchor="middle">Marlowe</text>

        <text class="beer-name"><textPath href="#beerArc" startOffset="50%" text-anchor="middle">Tindra Pale Ale</textPath></text>
      </symbol>
    </defs>
  </svg>

  <svg class="label label--brick" viewBox="0 0 520 460" role="img" aria-label="Tindra Pale Ale label, brick colourway"><use href="#beerLabel"/></svg>
  <svg class="label label--sage"  viewBox="0 0 520 460" role="img" aria-label="Tindra Pale Ale label, sage colourway"><use href="#beerLabel"/></svg>
  <svg class="label label--slate" viewBox="0 0 520 460" role="img" aria-label="Tindra Pale Ale label, slate colourway"><use href="#beerLabel"/></svg>
  <svg class="label label--amber" viewBox="0 0 520 460" role="img" aria-label="Tindra Pale Ale label, amber colourway"><use href="#beerLabel"/></svg>

</main>
</body>
</html>
```